Power Point for a new training package

I am a new business and about to offer my first teaching day. I have all the content, have a logo etc. but need to translate this into a slick bespoke Power Point presentation,

Target Market(s)

Senior people in healthcare sector, UK

Industry/Entity Type

Healthcare

Requirements
Must have
• Sense of originality, use of my logo and associated colour scheme, stylish but simple

```html
<!DOCTYPE html>
<html lang="en">
<head>
<meta charset="utf-8">
<title>Meridian Ward Consulting – Workshop Deck</title>
<link href="https://fonts.googleapis.com/css2?family=Montserrat:wght@300;400;600;700;800&family=Poppins:wght@300;400;500;600&display=swap" rel="stylesheet">
<style>
:root{
  --teal:#1fb3ad;
  --teal-dark:#169a95;
  --teal-light:#5fd6cf;
  --teal-pale:#e6f5f4;
  --ink:#1b1b1b;
  --body:#555c5c;
  --page:#e4e9e9;
  --slide:#fbfcfc;
  --white:#ffffff;
}
*{box-sizing:border-box;margin:0;padding:0}
html,body{width:1026px;height:1200px;overflow:hidden;background:var(--page)}
body{position:relative;font-family:"Poppins",sans-serif;color:var(--ink)}
.slide{position:absolute;width:443px;height:249px;background:var(--slide);overflow:hidden;box-shadow:0 4px 10px rgba(0,0,0,.12)}
.col-a{left:51px}.col-b{left:531px}
.row-1{top:54px}.row-2{top:335px}.row-3{top:616px}.row-4{top:896px}

.title{position:absolute;left:26px;top:13px;font-family:"Montserrat",sans-serif;font-size:14px;line-height:17px;letter-spacing:.3px;text-transform:uppercase}
.title b{font-weight:800;display:block}
.title span{font-weight:400;display:block}
.rule{position:absolute;left:0;top:52px;width:74px;height:1.5px;background:var(--teal)}
.rule::after{content:"";position:absolute;right:-4px;top:-3.5px;width:8px;height:8px;border-radius:50%;background:var(--teal)}

.brand{position:absolute;right:27px;top:7px;width:64px;text-align:center;font-family:"Poppins",sans-serif;font-weight:500;font-size:7px;line-height:8px;color:var(--ink)}
.brand i{display:block;margin:0 auto 3px;width:22px;height:22px;border:1.6px solid var(--teal);border-radius:50%}

.footer{position:absolute;left:0;right:0;top:230px;height:15px;background:var(--teal);color:var(--white);font-size:5px;display:flex;align-items:center;padding-left:25px;gap:6px}
.footer svg{width:5px;height:5px;fill:var(--white);vertical-align:-1px;margin-right:2px}
.footer .page{position:absolute;right:26px;top:1.5px;width:12px;height:12px;border-radius:50%;background:var(--white);color:var(--ink);font-weight:600;font-size:4.5px;display:flex;align-items:center;justify-content:center}

.photo{position:absolute;background:linear-gradient(135deg,#4fa7b1,#c7dde0 55%,#7fb2bf)}
.icon-disc{position:absolute;border-radius:50%;background:var(--teal);display:flex;align-items:center;justify-content:center}
.icon-disc svg{fill:none;stroke:var(--white);stroke-width:1.6;stroke-linecap:round;stroke-linejoin:round}
.label{font-size:6.5px;font-weight:600;text-transform:uppercase;color:var(--ink)}
.copy{font-size:5.3px;line-height:8.6px;color:var(--body)}

/* cover */
.cover-photo{left:0;top:21px;width:260px;height:207px;border-radius:0 110px 110px 0;background:linear-gradient(120deg,#138f8a,#1fb3ad 50%,#63c9c2)}
.cover-ring{position:absolute;left:212px;top:22px;width:204px;height:204px;border-radius:50%;background:rgba(31,179,173,.12)}
.cover-circle{position:absolute;left:217px;top:27px;width:194px;height:194px;border-radius:50%;background:var(--teal-pale);border:1.5px solid var(--teal);text-align:center;padding-top:17px}
.cover-circle .brand{position:static;margin:0 auto;width:auto;font-size:8.5px;line-height:10px}
.cover-circle .brand i{width:30px;height:30px;margin-bottom:4px}
.cover-headline{margin-top:10px;font-family:"Montserrat",sans-serif;font-size:14px;line-height:18px;text-transform:uppercase}
.cover-headline b{font-weight:700}
.cover-headline span{font-weight:400}

/* divider */
.divider-text{position:absolute;left:0;right:0;top:108px;text-align:center;font-family:"Montserrat",sans-serif;font-size:25px;letter-spacing:.5px}
.divider-text b{font-weight:800}.divider-text span{font-weight:400}

/* steps */
.step{position:absolute;top:73px;width:120px;text-align:center}
.step-num{position:absolute;left:4px;top:4px;font-family:"Montserrat",sans-serif;font-weight:300;font-size:50px;line-height:50px;color:transparent;-webkit-text-stroke:1.3px var(--teal)}
.step-ring{position:absolute;left:42px;top:0;width:69px;height:69px;border-radius:50%;border:1.4px solid var(--teal);background:var(--white);display:flex;align-items:center;justify-content:center}
.step-ring::before{content:"";position:absolute;left:3px;top:4px;width:5px;height:5px;border-radius:50%;background:var(--teal)}
.step .label{position:absolute;top:75px;left:0;right:0}
.step .copy{position:absolute;top:88px;left:2px;right:2px}
.step-arrow{position:absolute;stroke:#cfd6d6;fill:none;stroke-width:2}

/* governance */
.hub{position:absolute;left:57px;top:87px;width:104px;height:104px;border-radius:50%;background:var(--white);box-shadow:0 3px 10px rgba(0,0,0,.12);text-align:center;padding-top:22px}
.hub .brand{position:static;width:auto;font-size:9px;line-height:10px}
.hub .brand i{width:30px;height:30px;margin-bottom:3px}
.gov-item{position:absolute;width:160px}
.gov-item .label{margin-bottom:4px;font-size:6px}

/* structure */
.structure-photo{left:26px;top:69px;width:191px;height:149px;border-radius:14px;border:3px solid var(--white);box-shadow:0 2px 8px rgba(0,0,0,.15);background:linear-gradient(120deg,#2f5f85,#8fb2cc 50%,#e7eef3)}
.structure-copy{position:absolute;left:247px;top:88px;width:170px}
.structure-copy p+p{margin-top:6px}

/* cards */
.card{position:absolute;top:93px;width:120px;height:115px;border:1.3px solid var(--teal);border-radius:6px;background:var(--white);box-shadow:0 3px 6px rgba(0,0,0,.08);padding:29px 11px 0}
.card .icon-disc{left:12px;top:-18px;width:34px;height:34px}
.card .label{font-size:7.5px;margin-bottom:6px}

/* timeline */
.timeline{position:absolute;left:67px;top:141px;width:309px;height:1px;background:#cfd6d6}
.timeline::before,.timeline::after{content:"";position:absolute;top:-4px;width:9px;height:9px;border-radius:50%;border:1.3px solid #cfd6d6;background:var(--white)}
.timeline::before{left:-4px}.timeline::after{right:-4px}
.tl-node{position:absolute;top:126px;width:30px;height:30px;box-shadow:0 0 0 3px rgba(31,179,173,.18)}
.tl-stem{position:absolute;width:0;border-left:1px dashed var(--teal);height:18px}
.tl-text{position:absolute;width:96px;text-align:center}
.tl-text .label{font-size:5.5px;margin-bottom:3px}
.tl-text .copy{font-size:4.6px;line-height:7.4px}

/* thank you */
.ty-photo{left:229px;top:0;width:214px;height:208px;border-radius:0 0 0 150px/0 0 0 130px;background:linear-gradient(135deg,#9fc5d6,#e9dccd 55%,#6f8f8c)}
.ty-photo-mask{position:absolute;left:229px;top:0;width:214px;height:208px;clip-path:ellipse(100% 80% at 100% 30%)}
.ty-inset{position:absolute;left:236px;top:120px;width:80px;height:80px;border-radius:50%;border:3px solid var(--white);background:linear-gradient(135deg,#15948f,#3fbdb6)}
.ty-title{position:absolute;left:26px;top:56px;font-family:"Montserrat",sans-serif;font-size:15px}
.ty-title b{font-weight:800}.ty-title span{font-weight:400}
.contact{position:absolute;left:25px;display:flex;align-items:center;gap:10px;font-size:8px;color:var(--ink)}
.contact .icon-disc{position:static;width:22px;height:22px}
.follow{position:absolute;left:25px;top:222px;display:flex;align-items:center;gap:3px;font-size:6.8px;font-weight:600}
.follow .label{font-size:6.8px;margin-right:5px}
.social{width:16px;height:16px;border-radius:50%;border:1px solid var(--teal)}
</style>
</head>
<body>

<!-- Cover -->
<section class="slide col-a row-1">
  <div class="photo cover-photo" role="img" aria-label="Pharmacist in a lab coat handling medicine boxes, teal tinted"></div>
  <div class="cover-ring"></div>
  <div class="cover-circle">
    <div class="brand"><i></i>Meridian Ward<br>Consulting</div>
    <div class="cover-headline"><b>Explore your<br>pharmacy career<br>options</b> <span>with<br>our interactive<br>workshops</span></div>
  </div>
</section>

<!-- Section divider -->
<section class="slide col-b row-1">
  <div class="brand"><i></i>Meridian Ward<br>Consulting</div>
  <div class="divider-text"><b>SECTION</b> <span>DIVIDER</span></div>
  <div class="footer">
    <span><svg viewBox="0 0 10 10"><path d="M2 0l2 2-1 1.5q1 2 3 3L7.5 5.5l2 2-1.5 2Q4 9 .5 2z"/></svg>+44 (0) 7700 900123</span><span>|</span>
    <span><svg viewBox="0 0 10 10"><path d="M0 2h10v6H0z"/></svg>info@meridianwardconsulting.com</span>
    <span class="page">05</span>
  </div>
</section>

<!-- Applying -->
<section class="slide col-a row-2">
  <h2 class="title"><b>Applying to</b><span>Hospital pharmacy jobs</span></h2>
  <div class="rule"></div>
  <div class="brand"><i></i>Meridian Ward<br>Consulting</div>

  <div class="step" style="left:26px">
    <div class="step-num">1</div>
    <div class="step-ring"><svg width="22" height="22" viewBox="0 0 24 24"><path d="M4 22V9h16v13H4zM9 22v-5h6v5M10 4h4v4h-4zM12 4.5v3M10.5 6h3" fill="none" stroke="#1b1b1b" stroke-width="2"/></svg></div>
    <div class="label">Lorem ipsum dolor</div>
    <div class="copy">Lorem ipsum dolor sit amet, conse ctetur adipiscing elit, sed do eiusmo tempor incididunt ut labore et eiusmod sed aliqua.</div>
  </div>
  <svg class="step-arrow" style="left:125px;top:108px" width="50" height="28" viewBox="0 0 50 28"><path d="M2 24q24 6 44-18M40 6h7v7"/></svg>

  <div class="step" style="left:163px">
    <div class="step-num">2</div>
    <div class="step-ring"><svg width="22" height="22" viewBox="0 0 24 24"><path d="M5 2h12v20H5z" fill="#1b1b1b"/><path d="M8 7h6M8 11h6M8 15h3" stroke="#fff" stroke-width="1.5"/><circle cx="18" cy="18" r="4.5" fill="#1b1b1b" stroke="#fff"/><path d="M16 18l1.5 1.5 3-3" stroke="#fff" stroke-width="1.2" fill="none"/></svg></div>
    <div class="label">Lorem ipsum dolor</div>
    <div class="copy">Lorem ipsum dolor sit amet, conse ctetur adipiscing elit, sed do eiusmo tempor incididunt ut labore et eiusmod sed aliqua.</div>
  </div>
  <svg class="step-arrow" style="left:262px;top:82px" width="50" height="28" viewBox="0 0 50 28"><path d="M2 12q22-14 44 2M40 8l6 6-7 3"/></svg>

  <div class="step" style="left:300px">
    <div class="step-num">3</div>
    <div class="step-ring"><svg width="22" height="22" viewBox="0 0 24 24"><circle cx="10" cy="10" r="7" fill="none" stroke="#1b1b1b" stroke-width="2.5"/><path d="M15 15l6 6" stroke="#1b1b1b" stroke-width="3"/><circle cx="10" cy="8" r="2" fill="#1b1b1b"/><path d="M6.5 13q3.5-3 7 0" fill="#1b1b1b"/></svg></div>
    <div class="label">Lorem ipsum dolor</div>
    <div class="copy">Lorem ipsum dolor sit amet, conse ctetur adipiscing elit, sed do eiusmo tempor incididunt ut labore et eiusmod sed aliqua.</div>
  </div>

  <div class="footer">
    <span><svg viewBox="0 0 10 10"><path d="M2 0l2 2-1 1.5q1 2 3 3L7.5 5.5l2 2-1.5 2Q4 9 .5 2z"/></svg>+44 (0) 7700 900123</span><span>|</span>
    <span><svg viewBox="0 0 10 10"><path d="M0 2h10v6H0z"/></svg>info@meridianwardconsulting.com</span>
    <span class="page">02</span>
  </div>
</section>

<!-- Governance -->
<section class="slide col-b row-2">
  <h2 class="title"><b>Governance, safety, and</b><span>Regulation around medicines</span></h2>
  <div class="rule"></div>
  <div class="brand"><i></i>Meridian Ward<br>Consulting</div>

  <svg style="position:absolute;left:150px;top:60px" width="50" height="160" viewBox="0 0 50 160"><path d="M6 2q70 78 0 156" fill="none" stroke="#444" stroke-width=".7" stroke-dasharray="3 2"/></svg>
  <div class="hub"><div class="brand"><i></i>Meridian Ward<br>Consulting</div></div>

  <div class="icon-disc" style="left:160px;top:74px;width:32px;height:32px"><svg width="14" height="14" viewBox="0 0 24 24"><path d="M3 9l9-5 9 5M5 10v8M10 10v8M14 10v8M19 10v8M3 20h18"/></svg></div>
  <div class="icon-disc" style="left:175px;top:124px;width:32px;height:32px;background:var(--teal-light)"><svg width="14" height="14" viewBox="0 0 24 24"><path d="M12 3l8 3v6q0 6-8 9-8-3-8-9V6z"/><path d="M9 12l2 2 4-4"/></svg></div>
  <div class="icon-disc" style="left:161px;top:174px;width:32px;height:32px;background:var(--teal-light)"><svg width="14" height="14" viewBox="0 0 24 24"><path d="M6 3h9l3 3v14H6z"/><path d="M9 9h6M9 13h6M9 17h3"/></svg></div>

  <div class="gov-item" style="left:208px;top:71px"><div class="label">Governance</div><div class="copy">Lorem ipsum dolor sit amet, consectetur adipiscing elit, sed do eiusmod tempor incididunt ut labore et dolore magna aliqua.</div></div>
  <div class="gov-item" style="left:222px;top:120px"><div class="label">Safety</div><div class="copy">Lorem ipsum dolor sit amet, consectetur adipiscing elit, sed do eiusmod tempor incididunt ut labore et dolore magna aliqua.</div></div>
  <div class="gov-item" style="left:208px;top:171px"><div class="label">Regulation</div><div class="copy">Lorem ipsum dolor sit amet, consectetur adipiscing elit, sed do eiusmod tempor incididunt ut labore et dolore magna aliqua.</div></div>

  <div class="footer">
    <span><svg viewBox="0 0 10 10"><path d="M2 0l2 2-1 1.5q1 2 3 3L7.5 5.5l2 2-1.5 2Q4 9 .5 2z"/></svg>+44 (0) 7700 900123</span><span>|</span>
    <span><svg viewBox="0 0 10 10"><path d="M0 2h10v6H0z"/></svg>info@meridianwardconsulting.com</span>
    <span class="page">06</span>
  </div>
</section>

<!-- Structure -->
<section class="slide col-a row-3">
  <h2 class="title"><b>Hospital pharmacy</b><span>Structure and operation</span></h2>
  <div class="rule"></div>
  <div class="brand"><i></i>Meridian Ward<br>Consulting</div>
  <div class="photo structure-photo" role="img" aria-label="Two pharmacists in lab coats reviewing data on a monitor in a laboratory"></div>
  <div class="structure-copy copy">
    <p>Lorem ipsum dolor sit amet, consectetur adipiscing elit, sed do eiusmod tempor incididunt ut labore et dolore magna aliqua. Ut enim ad minim veniam, quis nostrud exercitation ullamco laboris nisi ut aliquip ex ea commodo consequat. Duis aute irure dolor in reprehenderit in voluptate velit esse cillum dolore eu fugiat nulla pariaturea.</p>
    <p>Lorem ipsum dolor sit amet, consectetur adipiscing elit, sed do eiusmod tempor incididunt ut labore et dolore magna aliqua. Ut enim ad minim veniam, quis nostrud exercitation ullamco laboris nisi ut aliquip ex ea commodo consequat. Duis aute irure dolor in reprea.</p>
  </div>
  <div class="footer">
    <span><svg viewBox="0 0 10 10"><path d="M2 0l2 2-1 1.5q1 2 3 3L7.5 5.5l2 2-1.5 2Q4 9 .5 2z"/></svg>+44 (0) 7700 900123</span><span>|</span>
    <span><svg viewBox="0 0 10 10"><path d="M0 2h10v6H0z"/></svg>info@meridianwardconsulting.com</span>
    <span class="page">03</span>
  </div>
</section>

<!-- Preparation -->
<section class="slide col-b row-3">
  <h2 class="title"><b>Preparation for</b><span>Application and job interviews</span></h2>
  <div class="rule"></div>
  <div class="brand"><i></i>Meridian Ward<br>Consulting</div>

  <div class="card" style="left:25px">
    <div class="icon-disc"><svg width="15" height="15" viewBox="0 0 24 24"><path d="M6 3h9l3 3v15H6z"/><path d="M9 11h6M9 14h6M9 17h6"/></svg></div>
    <div class="label">Lorem ipsum</div>
    <div class="copy">Lorem ipsum dolor sit amet, consectetur adipiscing elit, sed do eiusmod tempor incididunt ut labore et dolore magna aliqua. Ut enim ad minim veniam, quis nostrud exercitation ullamco laboris nisi ut aliquipea.</div>
  </div>
  <div class="card" style="left:161px">
    <div class="icon-disc" style="background:#2ec2bb"><svg width="15" height="15" viewBox="0 0 24 24"><circle cx="8" cy="8" r="3"/><path d="M3 19q0-6 5-6t5 6"/><path d="M13 4h8v6h-8z"/><circle cx="17" cy="14" r="2.5"/><path d="M13 21q0-4 4-4t4 4"/></svg></div>
    <div class="label">Lorem ipsum</div>
    <div class="copy">Lorem ipsum dolor sit amet, consectetur adipiscing elit, sed do eiusmod tempor incididunt ut labore et dolore magna aliqua. Ut enim ad minim veniam, quis nostrud exercitation ullamco laboris nisi ut aliquipea.</div>
  </div>
  <div class="card" style="left:297px">
    <div class="icon-disc" style="background:var(--teal-light)"><svg width="15" height="15" viewBox="0 0 24 24"><path d="M4 3h10v14H4z"/><path d="M7 7h4M7 10h4"/><path d="M12 13h9v8h-9zM15 13v-2h3v2"/></svg></div>
    <div class="label">Lorem ipsum</div>
    <div class="copy">Lorem ipsum dolor sit amet, consectetur adipiscing elit, sed do eiusmod tempor incididunt ut labore et dolore magna aliqua. Ut enim ad minim veniam, quis nostrud exercitation ullamco laboris nisi ut aliquipea.</div>
  </div>

  <div class="footer">
    <span><svg viewBox="0 0 10 10"><path d="M2 0l2 2-1 1.5q1 2 3 3L7.5 5.5l2 2-1.5 2Q4 9 .5 2z"/></svg>+44 (0) 7700 900123</span><span>|</span>
    <span><svg viewBox="0 0 10 10"><path d="M0 2h10v6H0z"/></svg>info@meridianwardconsulting.com</span>
    <span class="page">07</span>
  </div>
</section>

<!-- Day in the life -->
<section class="slide col-a row-4">
  <h2 class="title"><b>A day in the</b><span>Life of a hospital pharmacist</span></h2>
  <div class="rule"></div>
  <div class="brand"><i></i>Meridian Ward<br>Consulting</div>

  <div class="timeline"></div>

  <div class="tl-text" style="left:74px;top:64px"><div class="label">Lorem ipsum</div><div class="copy">Lorem ipsum dolor sit amet, consectetur adipiscing elit, sed do eiusmod tempor incididunt ut laborea.</div></div>
  <div class="tl-stem" style="left:122px;top:105px"></div>
  <div class="icon-disc tl-node" style="left:107px"><svg width="13" height="13" viewBox="0 0 24 24"><path d="M4 21V8h16v13M9 21v-4h6v4M10 3h4v4h-4zM8 11h2M14 11h2M8 14h2M14 14h2"/></svg></div>

  <div class="icon-disc tl-node" style="left:172px;background:#2ec2bb"><svg width="13" height="13" viewBox="0 0 24 24"><path d="M8 3h8v3H8zM6 6h12v15H6z"/><path d="M12 10v6M9 13h6"/></svg></div>
  <div class="tl-stem" style="left:187px;top:159px"></div>
  <div class="tl-text" style="left:139px;top:188px"><div class="label">Lorem ipsum</div><div class="copy">Lorem ipsum dolor sit amet, consectetur adipiscing elit, sed do eiusmod tempor incididunt ut laborea.</div></div>

  <div class="tl-text" style="left:203px;top:64px"><div class="label">Lorem ipsum</div><div class="copy">Lorem ipsum dolor sit amet, consectetur adipiscing elit, sed do eiusmod tempor incididunt ut laborea.</div></div>
  <div class="tl-stem" style="left:251px;top:105px"></div>
  <div class="icon-disc tl-node" style="left:236px;background:#44ccc4"><svg width="13" height="13" viewBox="0 0 24 24"><path d="M12 22s-7-7-7-12a7 7 0 0114 0c0 5-7 12-7 12z"/><path d="M12 7v6M9 10h6"/></svg></div>

  <div class="icon-disc tl-node" style="left:301px;background:var(--teal-light)"><svg width="13" height="13" viewBox="0 0 24 24"><path d="M12 3v18M8 7q4-3 8 0t-8 5 8 5"/></svg></div>
  <div class="tl-stem" style="left:316px;top:159px"></div>
  <div class="tl-text" style="left:268px;top:188px"><div class="label">Lorem ipsum</div><div class="copy">Lorem ipsum dolor sit amet, consectetur adipiscing elit, sed do eiusmod tempor incididunt ut laborea.</div></div>

  <div class="footer">
    <span><svg viewBox="0 0 10 10"><path d="M2 0l2 2-1 1.5q1 2 3 3L7.5 5.5l2 2-1.5 2Q4 9 .5 2z"/></svg>+44 (0) 7700 900123</span><span>|</span>
    <span><svg viewBox="0 0 10 10"><path d="M0 2h10v6H0z"/></svg>info@meridianwardconsulting.com</span>
    <span class="page">04</span>
  </div>
</section>

<!-- Thank you -->
<section class="slide col-b row-4">
  <div class="photo ty-photo" role="img" aria-label="Pharmacist consulting with a patient, showing information on a tablet"></div>
  <div class="ty-inset" role="img" aria-label="Pharmacist working at a laboratory bench, teal tinted"></div>
  <div class="brand" style="left:26px;right:auto;top:7px"><i></i>Meridian Ward<br>Consulting</div>
  <h2 class="ty-title"><b>THANK</b> <span>YOU</span></h2>
  <div class="rule" style="top:79px;width:58px"></div>

  <div class="contact" style="top:100px"><span class="icon-disc"><svg width="10" height="10" viewBox="0 0 24 24"><path d="M5 3l4 4-2 3q2 4 7 7l3-2 4 4-3 3Q7 21 2 6z" fill="#fff" stroke="none"/></svg></span>+44 (0) 7700 900123</div>
  <div class="contact" style="top:128px"><span class="icon-disc"><svg width="10" height="10" viewBox="0 0 24 24"><path d="M2 5h20v14H2z" fill="#fff" stroke="none"/><path d="M2 5l10 8 10-8" stroke="#1fb3ad"/></svg></span>info@meridianwardconsulting.com</div>
  <div class="contact" style="top:156px"><span class="icon-disc"><svg width="10" height="10" viewBox="0 0 24 24"><path d="M12 22s-7-7-7-12a7 7 0 0114 0c0 5-7 12-7 12z" fill="#fff" stroke="none"/><circle cx="12" cy="10" r="2.5" fill="#1fb3ad" stroke="none"/></svg></span>12 Harbour Lane, London EC1A 4XY</div>
  <div class="contact" style="top:183px"><span class="icon-disc"><svg width="10" height="10" viewBox="0 0 24 24"><circle cx="12" cy="12" r="9"/><path d="M3 12h18M12 3q5 9 0 18M12 3q-5 9 0 18"/></svg></span>https://meridianwardconsulting.com/</div>

  <div class="follow"><span class="label">Follow us on:</span><span class="social"></span><span class="social"></span><span class="social"></span></div>
</section>

</body>
</html>
```